Sports industries business card with professional design

We need to design a business card for our company based in Singapore. We are looking for a better quality design for our business card. Our company, Motion the Edge, is a sports services provider which focus on Strength and Conditioning coaching as well as Wushu Coaching. We are looking for 2 set of business card, 1 for strength and conditioning and another for Wushu.

Contact Information for Business Card

Address: Kew Tai Industrial Building, 27 Brookfield Road #04-12 Singapore 641382
ACRA: 48715209K
Tel: 91248637 / 86371425
Facebook: https://www.facebook.com/Motion.the.Edge
Website: www.motion.the.edgeexample
email: motion.the.edge@mailbox-example.com

Requirements
Nice to have
• Bsc. Exercise and Sports Science

```html
<!DOCTYPE html>
<html lang="en">
<head>
<meta charset="utf-8">
<title>Motion the Edge – Business Card</title>
<link href="https://fonts.googleapis.com/css2?family=Roboto:wght@400;500&display=swap" rel="stylesheet">
<style>
  :root {
    --backdrop: #141414;
    --card: #1e1e1e;
    --card-edge: #2a2a2a;
    --ink: #d9d9d9;
    --ink-soft: #a8a8a8;
    --rule: #5a5a5a;
  }
  * { margin: 0; padding: 0; box-sizing: border-box; }
  html, body { width: 1200px; height: 900px; overflow: hidden; }
  body {
    background: var(--backdrop);
    font-family: "Roboto", Arial, sans-serif;
    color: var(--ink);
    display: flex;
    flex-direction: column;
    align-items: center;
    justify-content: center;
    gap: 40px;
  }
  .card {
    width: 700px;
    height: 400px;
    background: var(--card);
    border: 1px solid var(--card-edge);
    position: relative;
  }
  .brand {
    font-weight: 500;
    color: var(--ink);
    text-transform: uppercase;
    line-height: 1;
  }
  .brand-word { display: block; letter-spacing: 2px; }
  .brand-tag { display: block; letter-spacing: 9px; }

  .card-front { display: flex; align-items: center; justify-content: center; }
  .card-front .brand { text-align: center; }
  .card-front .brand-word { font-size: 72px; }
  .card-front .brand-tag { font-size: 24px; margin-top: 8px; }

  .card-back { display: flex; align-items: center; }
  .card-back .brand { width: 390px; text-align: center; }
  .card-back .brand-word { font-size: 58px; }
  .card-back .brand-tag { font-size: 19px; margin-top: 6px; letter-spacing: 7px; }
  .divider { width: 1px; height: 200px; background: var(--rule); }
  .contact { padding-left: 36px; }
  .person-name { font-size: 27px; font-weight: 400; letter-spacing: 2px; text-transform: uppercase; }
  .person-role { font-size: 15px; color: var(--ink-soft); margin-top: 4px; }
  .address { font-size: 16px; line-height: 1.4; margin-top: 18px; }
  .lines { list-style: none; margin-top: 14px; font-size: 16px; line-height: 1.55; }
  .lines li { display: flex; align-items: center; gap: 10px; }
  .lines svg { width: 12px; height: 12px; flex: none; }
</style>
</head>
<body>
  <section class="card card-front">
    <div class="brand">
      <span class="brand-word">Motion</span>
      <span class="brand-tag">The Edge</span>
    </div>
  </section>

  <section class="card card-back">
    <div class="brand">
      <span class="brand-word">Motion</span>
      <span class="brand-tag">The Edge</span>
    </div>
    <div class="divider"></div>
    <div class="contact">
      <h1 class="person-name">Darren Koh</h1>
      <p class="person-role">Founder &amp; CEO</p>
      <p class="address">27 Brookfield Road #04-12<br>Singapore 641382</p>
      <ul class="lines">
        <li>
          <svg viewBox="0 0 12 12" aria-hidden="true"><path d="M3 1 L5 3.5 L4 5 Q5.5 7.5 7 8 L8.5 7 L11 9 L9.5 11 Q4 10 1 3 Z" fill="none" stroke="#a8a8a8" stroke-width="1"/></svg>
          9124 8637
        </li>
        <li>
          <svg viewBox="0 0 12 12" aria-hidden="true"><rect x="1" y="2.5" width="10" height="7" fill="none" stroke="#a8a8a8" stroke-width="1"/><path d="M1 2.5 L6 6.5 L11 2.5" fill="none" stroke="#a8a8a8" stroke-width="1"/></svg>
          motion.the.edge@mailbox-example.com
        </li>
        <li>
          <svg viewBox="0 0 12 12" aria-hidden="true"><circle cx="6" cy="6" r="5" fill="none" stroke="#a8a8a8" stroke-width="1"/><ellipse cx="6" cy="6" rx="2.2" ry="5" fill="none" stroke="#a8a8a8" stroke-width="1"/><path d="M1 6 H11" stroke="#a8a8a8" stroke-width="1"/></svg>
          www.motion.the.edgeexample
        </li>
      </ul>
    </div>
  </section>
</body>
</html>
```